An hotel welcome folder kit
luxury suites in NYC
An hotel  welcome folder kit -
Creative Brief
We are looking for to set up a beautiful welcome folder for our suites guests. This folder will be placed in the room on the bed. Within this folder they will find the whole info they need in order to get around the building they are staying in,about our services, the location. amenities, attractions etc. here is some info about what our business about: Morvane Lodgings offers various luxury vacation suites in beautiful luxury residential buildings around Manhattan and are rented out to tourists on a short term basis a la a hotel. The suites and buildings come fully equipped with all the necessary amenities and more: - wireless internet & high definition television with digital cable in unit - On site laundry room - Fantastic fully equipped gym - Residential lounge area with billiards table - Amazing roof deck with breathtaking views of the city.
our suites guests.
The welcome kit is a folder that has a one pocket on the right hand side of the folder inside. in this pocket we will place the pages with the info the guests need to know. on the left hand side inside the folder we will pitch our hotel concept (1-2 short sentences). on the cover of the folder we would like to see our logo and the name of the hotel the logo file is attached. what do we need from you: 1.a design of the folder based on our logo (colors ans font) : cover , left hand side inside the folder, on the back of the folder our contact info 2. a design of a template for the pages that we will place inside the folder (each page has its own topic for example: one page is about our services, the second page is info about attractions in the city..etc) important: the design should present out consept of luxury , high end style, Cutting-Edge Unique/Creative,Clean/Simple, Sophisticated. info about the logo: Brown #CFBA76 R:207 G:186 B:118 Font:Rage Italic Font2: Arial tagline: Arial dark Gray: #333333 R:51 G:51 B:51 Thanks a lot!!!

```html
<!DOCTYPE html>
<html lang="en">
<head>
<meta charset="utf-8">
<title>Morvane Lodgings – Welcome Folder</title>
<link rel="stylesheet" href="https://fonts.googleapis.com/css2?family=Cinzel:wght@400&family=Pinyon+Script&family=Cormorant+Garamond:wght@400;500&family=Arimo:wght@400;700&display=swap">
<style>
  :root {
    --brown-dark: #3a2414;
    --brown-deep: #2d1b0e;
    --brown-mid: #4a3020;
    --gold: #cfba76;
    --gold-soft: #b99f5e;
    --tan: #c9ad78;
    --cream: #efe6d2;
    --night: #1d3a5c;
    --night-glow: #5e8fc0;
  }
  * { box-sizing: border-box; margin: 0; padding: 0; }
  html, body { width: 1200px; height: 394px; overflow: hidden; background: #ffffff; }
  .canvas { position: relative; width: 1200px; height: 394px; }

  .panel { position: absolute; background: var(--brown-dark); overflow: hidden; }
  .band {
    position: absolute; left: 0; right: 0; bottom: 0; height: 16px;
    background: linear-gradient(to bottom, var(--brown-deep), var(--brown-mid) 50%, var(--brown-deep));
    border-top: 1px solid var(--gold-soft);
  }

  /* Cover */
  .cover { left: 12px; top: 30px; width: 324px; height: 342px; }
  .cover-frame {
    position: absolute; left: 22px; top: 46px; width: 280px; height: 110px;
    border: 2px solid var(--gold); outline: 1px solid var(--gold-soft); outline-offset: 5px;
  }
  .cover-title {
    position: absolute; left: 22px; top: 46px; width: 280px; height: 110px;
    display: flex; align-items: center; justify-content: center; text-align: center;
    font-family: "Cinzel", serif; font-weight: 400; font-size: 20px; letter-spacing: 1px;
    white-space: nowrap; color: var(--gold);
  }

  /* Concept panel */
  .concept { left: 336px; top: 30px; width: 312px; height: 342px; border-left: 1px solid var(--brown-deep);
    background: radial-gradient(ellipse at 75% 55%, #4a3020 0%, var(--brown-dark) 60%); }
  .concept-heading {
    position: absolute; left: 14px; top: 54px;
    font-family: "Pinyon Script", cursive; font-weight: 400; font-size: 30px; color: var(--cream);
  }
  .concept-body {
    position: absolute; left: 18px; top: 104px; width: 282px;
    font-family: "Pinyon Script", cursive; font-size: 15px; line-height: 19px; color: var(--cream);
  }
  .brand { position: absolute; left: 50px; top: 268px; display: flex; align-items: center; gap: 8px; }
  .brand-dot { width: 14px; height: 14px; border-radius: 50%; background: var(--gold); }
  .brand-name { font-family: "Arimo", sans-serif; font-size: 15px; font-weight: 700; color: var(--gold); }
  .brand-tag { position: absolute; left: 72px; top: 290px; font-family: "Arimo", sans-serif; font-size: 7px; color: var(--cream); letter-spacing: 1px; }

  /* Right inside with pocket */
  .pocket-side { left: 828px; top: 24px; width: 360px; height: 348px; z-index: 1; }

  /* Insert page */
  .insert { position: absolute; left: 684px; top: 24px; width: 176px; height: 348px; background: var(--brown-dark); overflow: hidden; z-index: 2; box-shadow: 1px 0 3px rgba(0,0,0,0.4); }
  .insert-heading {
    position: absolute; left: 8px; top: 6px; width: 160px;
    font-family: "Cormorant Garamond", serif; font-weight: 400; font-size: 14.5px; line-height: 15px; color: var(--gold);
  }
  .insert-sub {
    position: absolute; left: 8px; top: 74px;
    font-family: "Cormorant Garamond", serif; font-weight: 500; font-size: 11px; color: var(--gold);
  }
  .insert-col {
    position: absolute; left: 8px; top: 92px; width: 72px;
    font-family: "Arimo", sans-serif; font-size: 5.6px; line-height: 8px; color: var(--cream);
  }
  .insert-photo {
    position: absolute; left: 86px; top: 92px; width: 84px; height: 104px;
    background: linear-gradient(to bottom, #0e2138 0%, var(--night) 45%, var(--night-glow) 78%, #1b3553 100%);
  }
  .insert-photo span {
    position: absolute; left: 6px; top: 5px; font-family: "Arimo", sans-serif; font-size: 6px; color: #ffffff;
  }
  .insert-foot {
    position: absolute; left: 8px; top: 226px; width: 160px;
    font-family: "Arimo", sans-serif; font-size: 5.6px; line-height: 8px; color: var(--cream);
  }

  .pocket { position: absolute; left: 830px; top: 24px; width: 80px; height: 348px; z-index: 3; }
  .contact {
    position: absolute; right: 16px; bottom: 30px; text-align: right; font-style: normal;
    font-family: "Arimo", sans-serif; font-size: 7px; line-height: 10px; color: var(--cream);
  }
  .contact strong { color: var(--gold); font-size: 8px; }
</style>
</head>
<body>
<div class="canvas">

  <section class="panel cover">
    <div class="cover-frame"></div>
    <h1 class="cover-title">MORVANE LODGINGS</h1>
    <div class="band"></div>
  </section>

  <section class="panel concept">
    <h2 class="concept-heading">About Morvane</h2>
    <p class="concept-body">Every stay begins with the quiet comfort of a home above the city. Our suites are set in fine residential buildings across Manhattan, fully furnished and ready for you. Enjoy a lounge with billiards, a modern gym and a roof deck with sweeping views of the skyline. We look after every detail so you can simply arrive, unwind and explore New York at your own pace.</p>
    <div class="brand"><span class="brand-dot"></span><span class="brand-name">Morvane Lodgings</span></div>
    <div class="brand-tag">Luxury Suites NYC</div>
    <div class="band"></div>
  </section>

  <section class="panel pocket-side">
    <address class="contact">
      <strong>Morvane Lodgings</strong><br>
      Address Line 1<br>
      Address Line 2<br>
      Tel: 000 000 0000<br>
      Fax: 000 000 0000<br>
      info@morvanelodgings.com<br>
      www.morvanelodgings.com
    </address>
    <div class="band"></div>
  </section>

  <article class="insert">
    <h2 class="insert-heading">Suites are spacious and had all the amenities that you need.</h2>
    <h3 class="insert-sub">Words about views</h3>
    <p class="insert-col">From the roof deck the whole of Manhattan opens up before you. Watch the towers glow at dusk, follow the river lights and spot the landmarks you plan to visit tomorrow. Chairs and shade are set out through the warmer months for every guest.</p>
    <div class="insert-photo" role="img" aria-label="Photograph of the Manhattan skyline lit up at night"><span>The suite views</span></div>
    <p class="insert-foot">The deck is open daily from early morning until late evening. Please ask the front desk for access cards, towels and any help you need during your stay with us.</p>
  </article>

  <svg class="pocket" viewBox="0 0 80 348" aria-hidden="true">
    <polygon points="0,250 80,210 80,348 0,348" fill="var(--tan)"/>
    <line x1="0" y1="250" x2="80" y2="210" stroke="#e2cd98" stroke-width="1"/>
  </svg>

</div>
</body>
</html>
```